Business card

I want a business card the looks like a credit card, must eye-catching !!! I attached some things that I did obviously I want it to LOOK WAY more professional than what I can do....Just some ideas.... that I was thinking

Contact Information for Business Card

Must look like a credit card, I attached some things that I did obviously I want it to LOOK WAY more professional than what I can do....Just some ideas.... that I was thinking

Requirements
Must have
• Must look like a credit card, I attached some things that I did obviously I want it to LOOK WAY more professional than what I can do....Just some ideas.... that I was thinking
Nice to have
Should not have

```html
<!DOCTYPE html>
<html lang="en">
<head>
<meta charset="utf-8">
<title>Northvale Capital – Business Card</title>
<link href="https://fonts.googleapis.com/css2?family=Aldrich&family=Exo+2:ital,wght@0,600;0,700;0,800;1,800&display=swap" rel="stylesheet">
<style>
  :root {
    --page-bg: #e6e7e8;
    --card-bg: #0c0d0f;
    --map-tone-a: rgba(90, 96, 104, 0.22);
    --map-tone-b: rgba(60, 64, 70, 0.06);
    --white: #ffffff;
    --yellow: #fcc916;
    --navy: #23406e;
    --chip-a: #f4d77a;
    --chip-b: #b88a1f;
    --sig-bg: #dcdcdc;
    --social-a: #1a5c8a;
    --social-b: #8fb7e2;
    --social-c: #1a9ad6;
  }
  * { box-sizing: border-box; margin: 0; padding: 0; }
  html, body { width: 1200px; height: 635px; overflow: hidden; background: var(--page-bg); }
  body { position: relative; font-family: "Exo 2", sans-serif; color: var(--white); }

  .card {
    position: absolute; top: 190px; width: 445px; height: 254px;
    background: var(--card-bg); border-radius: 20px; overflow: hidden;
    box-shadow: 0 6px 10px rgba(0,0,0,0.25);
  }
  .card--front { left: 128px; }
  .card--back { left: 628px; }

  .world-map {
    position: absolute; left: 20px; top: 18px; width: 410px; height: 230px;
    background: radial-gradient(ellipse at 55% 40%, var(--map-tone-a), var(--map-tone-b) 70%, transparent 100%);
  }

  .brand {
    position: absolute; font-family: "Exo 2", sans-serif; font-weight: 800;
    font-size: 24px; line-height: 1; color: var(--yellow); letter-spacing: 0.3px; white-space: nowrap;
  }
  .card--front .brand { left: 20px; top: 27px; }
  .card--back .brand { left: 29px; top: 193px; }

  .chip {
    position: absolute; left: 50px; top: 92px; width: 46px; height: 41px; border-radius: 6px;
    background: linear-gradient(135deg, var(--chip-a), var(--chip-b));
  }

  .card-number {
    position: absolute; left: 50px; top: 140px; width: 348px;
    display: flex; justify-content: space-between;
    font-family: "Aldrich", sans-serif; font-size: 29px; letter-spacing: 1px;
  }
  .expiry-label { position: absolute; left: 192px; top: 177px; font-family: "Aldrich", sans-serif; font-size: 9px; }
  .expiry { position: absolute; left: 159px; top: 192px; display: flex; align-items: center; gap: 6px; font-family: "Aldrich", sans-serif; }
  .expiry__hint { font-size: 8px; line-height: 0.95; }
  .expiry__date { font-size: 22px; letter-spacing: 1px; }

  .holder { position: absolute; left: 20px; top: 223px; font-family: "Aldrich", sans-serif; font-size: 14.5px; letter-spacing: 0.3px; white-space: nowrap; }
  .card-type { position: absolute; right: 23px; top: 220px; font-weight: 800; font-style: italic; font-size: 17px; color: var(--yellow); letter-spacing: 0.5px; }

  .slogan-band {
    position: absolute; left: 0; top: 25px; width: 100%; height: 57px; background: var(--white);
    display: flex; align-items: center; justify-content: center;
  }
  .slogan { font-weight: 600; font-size: 20.5px; color: var(--navy); letter-spacing: 0.2px; }

  .signature-strip { position: absolute; left: 133px; top: 89px; width: 178px; height: 39px; background: var(--sig-bg); }
  .signature-label { position: absolute; left: 133px; top: 132px; font-family: "Aldrich", sans-serif; font-size: 7.5px; }
  .email { position: absolute; left: 0; width: 100%; top: 144px; text-align: center; font-weight: 600; font-size: 17.5px; letter-spacing: 0.3px; }
  .contact { position: absolute; left: 0; width: 100%; top: 167px; text-align: center; font-family: "Aldrich", sans-serif; font-size: 10px; }

  .social { position: absolute; left: 287px; top: 201px; display: flex; gap: 8px; }
  .social__item { width: 38px; height: 38px; border-radius: 50%; }
  .social__item--a { background: var(--social-a); }
  .social__item--b { background: var(--social-b); }
  .social__item--c { background: var(--social-c); }
</style>
</head>
<body>
  <section class="card card--front">
    <div class="world-map" role="img" aria-label="Faint dotted world map in the card background"></div>
    <div class="brand">Northvale Capital</div>
    <div class="chip" role="img" aria-label="Gold payment chip"></div>
    <div class="card-number"><span>0720</span><span>0104</span><span>0122</span><span>1208</span></div>
    <div class="expiry-label">MONTH/YEAR</div>
    <div class="expiry"><span class="expiry__hint">VALID<br>THRU</span><span class="expiry__date">12/50</span></div>
    <div class="holder">DANA WHITLOCK / 555-014-2290</div>
    <div class="card-type">CREDIT CARD</div>
  </section>

  <section class="card card--back">
    <div class="world-map" role="img" aria-label="Faint dotted world map in the card background"></div>
    <div class="slogan-band"><p class="slogan">Experience Better Credit Card Processing</p></div>
    <div class="signature-strip" role="img" aria-label="Signature panel with fine security print"></div>
    <div class="signature-label">AUTHORIZED SIGNATURE</div>
    <div class="email">northvalecapital@example.com</div>
    <div class="contact">CONTACT US: 555-014-2290</div>
    <div class="brand">Northvale Capital</div>
    <div class="social" aria-label="Social profiles">
      <span class="social__item social__item--a"></span>
      <span class="social__item social__item--b"></span>
      <span class="social__item social__item--c"></span>
    </div>
  </section>
</body>
</html>
```